Website for Sports and Exercise Medicine Doctor with active research in stem cells therapies.

I am a sports and exercise medicine doctor with research interests in the cutting edge areas of biological therapies, most notable stem cells. None of my patients are dying of anything, and most of them come to see me to decrease their pain, so they can get back to what they want to do.

The approach i then take is to decrease their pain and support them to achieve the things they wish to achieve. Most people start at "Just make it stop hurting doc" , but I try to move them towards something more important over time.

I would like the website to be very different to other "Doctor or medical websites" in its look. No pictures of doctors in white coats and no pictures of fit old people smiling. I would potentially like the fist thing seen to be a quote:

"Less pain. Everybody wants it, but what are you going to do, once you've got it?"

(But this is only an idea, I am open to anything)

The website will need a couple of things

1. "Locations" I work
2. "Research" I am involved in
3. "Sort Me out" - Clinical information for people to access
4. "Social" - imbedded chirpline and friendgrid
5. "Blog" - imbedded postmill blog
6. "Bio" - the usual bio-stuff

The "Sort Me out" - pages I would like to have the functionality as seen in this site http://www.vandrolix.com.au/platelet/. I intend to put disease topics into these pages (eg Achilles tehdinopathy, osteoarthritis etc etc etc). Once again I am not wedded to this but something along these lines would be good.

To give you an idea these are some sites I like
http://www.harborlantern.com/
http://quimbet.com/
http://orvanstudio.com.sg/
http://milbonhonestkettle.com/
http://www.tessmonthly.com/
http://gravwick.com/#offering
http://pelicanworks.tv/
http://tidalnova.com/
http://foxledger.co.uk/#about

Target Market(s)

20-80 year old.
People with tendon injuries
People with osteoarthritis
People interested in stem cells
I will build the site over time to contain information on multiple sporting injuries and musculoskeletal disorders. It will also become a site for the latest on stem cell research particularly in the area of osteoarthritis.

Industry/Entity Type

Medical

Font styles to use
Sans Serif

Colors
ffffff

Requirements
Nice to have
• To give you an idea these are some sites I like
http://quimbet.com/
http://pelicanworks.tv/
http://tidalnova.com/
Should not have
• Pictures of doctors in white coats or old fit people smiling

```html
<!DOCTYPE html>
<html lang="en">
<head>
<meta charset="utf-8">
<title>tolvane — Sports and Exercise Medicine</title>
<link rel="stylesheet" href="https://fonts.googleapis.com/css2?family=Questrial&family=Dosis:wght@700&display=swap">
<style>
  :root {
    --sidebar: #0d3358;
    --sidebar-line: #15406a;
    --footer: #0b2c4c;
    --ink: #ffffff;
    --icon: #2f7fc4;
    --bubble-fill: rgba(150, 196, 226, 0.78);
    --bubble-edge: rgba(205, 230, 246, 0.9);
    --button: #1d6f96;
    --button-edge: #5ea9cb;
  }
  * { box-sizing: border-box; margin: 0; padding: 0; }
  html, body { width: 1200px; height: 749px; overflow: hidden; background: var(--sidebar); }
  body { position: relative; font-family: "Questrial", Arial, sans-serif; color: var(--ink); }

  .sidebar {
    position: absolute; left: 0; top: 0; width: 342px; height: 749px;
    background: var(--sidebar);
  }
  .sidebar-edge {
    position: absolute; left: 342px; top: 0; width: 2px; height: 749px; background: var(--ink);
  }
  .brand {
    position: absolute; left: 0; top: 22px; width: 342px; text-align: center;
    font-size: 46px; letter-spacing: 1px; color: var(--ink); line-height: 1;
  }
  .brand-rule { position: absolute; left: 90px; top: 98px; width: 252px; height: 1px; background: var(--sidebar-line); }

  .main-nav { position: absolute; left: 90px; top: 160px; width: 252px; list-style: none; }
  .main-nav li {
    position: relative; height: 37px; border-bottom: 1px solid var(--sidebar-line);
    display: flex; align-items: center; justify-content: flex-end; padding-right: 24px;
    font-size: 14.5px; letter-spacing: 0.4px;
  }
  .main-nav li:first-child { border-bottom: none; height: 36px; }
  .main-nav svg { position: absolute; left: 100px; top: 50%; transform: translateY(-50%); }

  .brand-watermark {
    position: absolute; left: 0; top: 470px; width: 342px; text-align: center;
    font-size: 96px; color: rgba(255,255,255,0.035); line-height: 1;
  }
  .sidebar-note {
    position: absolute; left: 96px; top: 702px; width: 222px; text-align: center;
    font-size: 10.5px; line-height: 12.5px;
  }

  .hero {
    position: absolute; left: 344px; top: 0; width: 856px; height: 698px;
    background:
      radial-gradient(ellipse 360px 260px at 432px 300px, #9cc4e0 0%, rgba(120,170,210,0.4) 55%, transparent 100%),
      radial-gradient(circle 110px at 140px 395px, #6fa0c8 0%, rgba(80,130,180,0) 100%),
      radial-gradient(circle 110px at 705px 395px, #6fa0c8 0%, rgba(80,130,180,0) 100%),
      radial-gradient(circle 75px at 200px 152px, #6c9ec6 0%, rgba(80,130,180,0) 100%),
      radial-gradient(circle 75px at 765px 152px, #6c9ec6 0%, rgba(80,130,180,0) 100%),
      linear-gradient(180deg, #3f77a8 0%, #5187b6 45%, #3a6d9d 100%);
  }
  .quote-bubble {
    position: absolute; left: 268px; top: 136px; width: 332px; height: 332px; border-radius: 50%;
    background: var(--bubble-fill); border: 3px solid var(--bubble-edge);
    box-shadow: 0 4px 18px rgba(20,60,100,0.35);
  }
  .quote {
    position: absolute; left: 0; top: 88px; width: 100%; text-align: center;
    font-size: 24px; line-height: 30px; font-weight: 400; padding: 0 12px;
  }
  .cta {
    position: absolute; left: 81px; top: 234px; width: 166px; height: 36px;
    background: var(--button); border: 1px solid var(--button-edge);
    font-family: "Dosis", Arial, sans-serif; font-weight: 700; font-size: 18px;
    letter-spacing: 0.6px; color: var(--ink); display: flex; align-items: center; justify-content: center;
  }

  .site-footer {
    position: absolute; left: 344px; top: 698px; width: 856px; height: 51px; background: var(--footer);
    font-size: 10.5px; letter-spacing: 0.2px;
  }
  .copyright { position: absolute; left: 21px; top: 18px; }
  .footer-nav { position: absolute; right: 89px; top: 18px; }
</style>
</head>
<body>
  <aside class="sidebar">
    <div class="brand">tolvane</div>
    <div class="brand-rule"></div>

    <ul class="main-nav">
      <li>SORT ME OUT
        <svg width="30" height="26" viewBox="0 0 30 26" fill="none" stroke="var(--icon)" stroke-width="2.4">
          <path d="M1 4h6v20h14V4h8"/><path d="M14 18V2M10 6l4-4 4 4"/>
        </svg>
      </li>
      <li>LOCATIONS
        <svg width="30" height="26" viewBox="0 0 30 26" fill="none" stroke="var(--icon)" stroke-width="2">
          <path d="M1 4l8-3 8 3 8-3v18l-8 3-8-3-8 3z"/><path d="M9 1v18M17 4v8"/>
          <circle cx="21" cy="15" r="3.5" fill="var(--icon)"/><path d="M21 18v6"/>
        </svg>
      </li>
      <li>RESEARCH
        <svg width="30" height="26" viewBox="0 0 30 26" fill="var(--icon)">
          <circle cx="15" cy="8" r="5"/><rect x="10" y="14" width="10" height="8" rx="3"/>
          <circle cx="4" cy="14" r="2.5"/><circle cx="26" cy="14" r="2.5"/>
          <rect x="2" y="17" width="4" height="6" rx="1.5"/><rect x="24" y="17" width="4" height="6" rx="1.5"/>
        </svg>
      </li>
      <li>SOCIAL
        <svg width="30" height="28" viewBox="0 0 30 28" fill="none" stroke="var(--icon)" stroke-width="2">
          <circle cx="15" cy="14" r="12"/><ellipse cx="15" cy="14" rx="5" ry="12"/><path d="M3 14h24M5 8h20M5 20h20"/>
        </svg>
      </li>
      <li>BLOG
        <svg width="30" height="24" viewBox="0 0 30 24" fill="var(--icon)">
          <rect x="5" y="2" width="20" height="20" rx="5"/>
        </svg>
      </li>
      <li>BIO
        <svg width="30" height="30" viewBox="0 0 30 30" fill="none" stroke="var(--icon)" stroke-width="2">
          <path d="M11 2h8M12 2v9L4 27h22l-8-16V2"/><path d="M7 21h16l3 6H4z" fill="var(--icon)"/>
        </svg>
      </li>
    </ul>

    <div class="brand-watermark" aria-hidden="true">tolvane</div>

    <p class="sidebar-note">vero eros et accumsan et iusto odio dignissim qui blandit praesent luptatum zzril delenit augue .</p>
  </aside>
  <div class="sidebar-edge"></div>

  <main class="hero" role="img" aria-label="Microscope view of translucent blue stem cells floating in fluid">
    <div class="quote-bubble">
      <p class="quote">Less pain. Everybody wants it, but what are you going to do, once you’ve got it?</p>
      <div class="cta">GET QUOTE NOW</div>
    </div>
  </main>

  <footer class="site-footer">
    <span class="copyright">COPYRIGHT 2013 TOLVANE.COM</span>
    <span class="footer-nav">SORT ME OUT | LOCATIONS | RESEARCH | SOCIAL | BLOG | BIO</span>
  </footer>
</body>
</html>
```